Modern Lawfirm Business Card Design

We're looking for a business card to incorporate the newly created logo we had made.

Ideally looking for a law firm business card demonstrating, modern, minimalist, strong/bold design.

I'm open to any design honestly, but nothing "flashy".

Target Market(s)

Immigration law, family immigration, humanitarian, general legal

Industry/Entity Type

Law Firm

Contact Information for Business Card

Please use dummy information, name, street address, city, state, phone number, email, website.

Font styles to use
Serif
Sans Serif

Requirements
Must have
• Please use dummy information, name, street address, city, state, phone number, email, website.

```html
<!DOCTYPE html>
<html lang="en">
<head>
<meta charset="UTF-8">
<title>Valcourt Immigration Law – Business Card</title>
<link rel="stylesheet" href="https://fonts.googleapis.com/css2?family=Montserrat:wght@400;500;700&display=swap">
<style>
  :root {
    --navy: #04467f;
    --white: #ffffff;
    --backdrop: #ececec;
    --ink: #3a3a3a;
    --muted: #9a9a9a;
  }
  * { margin: 0; padding: 0; box-sizing: border-box; }
  html, body { width: 1200px; height: 800px; overflow: hidden; }
  body {
    background: var(--backdrop);
    font-family: "Montserrat", Arial, sans-serif;
    position: relative;
  }
  .card {
    position: absolute;
    top: 250px;
    width: 520px;
    height: 300px;
    box-shadow: 0 4px 10px rgba(0,0,0,0.12);
  }
  .card--back {
    left: 60px;
    background: var(--navy);
    display: flex;
    align-items: center;
    justify-content: center;
  }
  .card--front {
    left: 620px;
    background: var(--white);
  }
  .firm-name {
    text-align: center;
    font-weight: 500;
    color: var(--white);
  }
  .firm-name__main {
    display: block;
    font-size: 50px;
    letter-spacing: 4px;
    line-height: 1;
  }
  .firm-name__sub {
    display: block;
    margin-top: 12px;
    font-size: 12px;
    letter-spacing: 9px;
  }
  .card--front .firm-name {
    position: absolute;
    left: 34px;
    top: 118px;
    color: var(--navy);
  }
  .card--front .firm-name__main { font-size: 30px; letter-spacing: 2px; }
  .card--front .firm-name__sub { font-size: 7.5px; letter-spacing: 5px; margin-top: 7px; }
  .details {
    position: absolute;
    left: 290px;
    top: 92px;
  }
  .details__name {
    font-weight: 700;
    font-size: 17px;
    color: var(--navy);
    letter-spacing: 0.3px;
  }
  .details__title {
    font-size: 12px;
    color: var(--muted);
    margin-top: 2px;
  }
  .details__address {
    font-size: 12px;
    color: var(--ink);
    margin-top: 18px;
    line-height: 1.5;
  }
  .details__contact {
    list-style: none;
    font-size: 12px;
    color: var(--ink);
    margin-top: 30px;
    line-height: 1.6;
  }
  .details__label { font-weight: 700; }
</style>
</head>
<body>
  <section class="card card--back" aria-label="Card back">
    <div class="firm-name">
      <span class="firm-name__main">VALCOURT</span>
      <span class="firm-name__sub">IMMIGRATION LAW</span>
    </div>
  </section>

  <section class="card card--front" aria-label="Card front">
    <div class="firm-name">
      <span class="firm-name__main">VALCOURT</span>
      <span class="firm-name__sub">IMMIGRATION LAW</span>
    </div>
    <div class="details">
      <p class="details__name">DANIEL REYES</p>
      <p class="details__title">Chief Executive Officer</p>
      <p class="details__address">Address Line 1<br>Address Line 2</p>
      <ul class="details__contact">
        <li><span class="details__label">PHONE:</span> 123 456 789</li>
        <li><span class="details__label">EMAIL:</span> name@email.com</li>
        <li><span class="details__label">WEB:</span> www.website.com</li>
      </ul>
    </div>
  </section>
</body>
</html>
```